Mexican Themed Party Invitations!

Hi,
We are wanting a Mexican themed party invititation for Dale's 40th!
We are wanting something that resembles an old Mexican postcard – like the ones you used to get in the 50’s–70's - the size would approximately be 7" by 5.5".
We would preferably like a double sided invite - The below details would be displayed on the back somewhere:
If there could also be room left somewhere on the back to attach a small magnet so that the invite can be stuck on the fridge:)
Dale's 40th
When: Saturday the 27th of July 2013 @ 7PM
Where: 48 Marlow Crescent, Coromandel Valley, SA
Bring: Yourself and cowboy drinkin’ boots
RSVP: Date, email and phone – make funny RSVP email address!
Dress: Preferably traditional Mexican or 70’s Cowboy/Girl – but tacky Sombrero’s and Ponchos are OK too!
Men: There will be a prize for the best grown (real) Mexican moustache
Music: by the Silver Cactus, Mexican Mariachi Band
Food: Supplied by……
Drinks: Bartender Trent will have the tequila shots and sangria ready to go
RSVP: by the 1st of July
Please note that we have attached some examples of pictures that we like as a bit of inspiration to give you a bit of an idea of which direction we are wanting to go in.
70's style would be good as Dale was born then.
We can't wait to see what you come up with!!!
Just for some inspration I found this image, which I love! If someone could do something like this, that would be awesome!
http://www.sales.pondvexel.com/items/r/r_mtp_lopez_card_81934.jpg
Dale's 40th insted of Juarez (or similar)

```html
<!DOCTYPE html>
<html lang="en">
<head>
<meta charset="utf-8">
<title>Dale's 40th! Invitation</title>
<link rel="stylesheet" href="https://fonts.googleapis.com/css2?family=Ultra&family=Rye&family=Yellowtail&family=Federo&family=Amaranth:ital,wght@0,400;0,700;1,700&display=swap">
<style>
  :root {
    --border-sand: #f3dca6;
    --teal: #8fe0d6;
    --teal-light: #a8ebe2;
    --teal-dark: #6ccfc4;
    --title-red: #e8402a;
    --cream: #fbf3dc;
    --ink: #1f2b2b;
    --shadow: #2e3f3f;
    --sketch-brown: #4a3a33;
  }
  * { margin: 0; padding: 0; box-sizing: border-box; }
  html, body { width: 1200px; height: 857px; overflow: hidden; background: var(--border-sand); }
  .invitation {
    position: relative;
    width: 1200px; height: 857px;
    background: var(--border-sand);
  }
  .postcard-back {
    position: absolute;
    left: 30px; top: 33px;
    width: 1138px; height: 789px;
    background: var(--teal);
    overflow: hidden;
  }
  .sunburst { position: absolute; inset: 0; width: 100%; height: 100%; }
  .illustration { position: absolute; border-radius: 10px; }
  .guitar-sketch {
    left: 72px; top: 5px; width: 160px; height: 305px;
    background: linear-gradient(180deg, rgba(74,58,51,.25), rgba(74,58,51,.45));
  }
  .cactus-sketch {
    left: 885px; top: 62px; width: 168px; height: 400px;
    background: linear-gradient(180deg, rgba(74,58,51,.3), rgba(74,58,51,.5));
  }
  .moustache-sketch {
    left: 805px; top: 622px; width: 280px; height: 66px;
    border-radius: 40px;
    background: var(--sketch-brown);
  }
  .title-name {
    position: absolute;
    left: 222px; top: 128px; width: 640px;
    text-align: center;
    font-family: "Ultra", "Rye", serif;
    font-weight: 400;
    font-size: 128px;
    line-height: 1;
    letter-spacing: -2px;
    color: var(--title-red);
    -webkit-text-stroke: 3px var(--cream);
    paint-order: stroke fill;
    text-shadow: 7px 8px 0 var(--shadow);
    transform: rotate(-2deg);
  }
  .title-age {
    position: absolute;
    left: 530px; top: 250px;
    font-family: "Yellowtail", cursive;
    font-size: 84px;
    line-height: 1;
    color: var(--cream);
    text-shadow: 4px 4px 0 var(--shadow);
    transform: rotate(-4deg);
  }
  .details {
    position: absolute;
    left: 107px; top: 370px;
    display: grid;
    grid-template-columns: 130px 6px 1fr;
    align-items: start;
  }
  .details-labels, .details-values { display: flex; flex-direction: column; }
  .details-labels span {
    font-family: "Federo", sans-serif;
    font-size: 33px; line-height: 42px;
    color: var(--ink);
    -webkit-text-stroke: 1px var(--ink);
  }
  .details-divider {
    margin-left: 25px;
    width: 5px; margin-top: 6px; height: 152px;
    background: var(--title-red);
    box-shadow: 3px 2px 0 var(--shadow);
  }
  .details-values { padding-left: 47px; }
  .details-values span {
    font-family: "Amaranth", sans-serif;
    font-weight: 400;
    font-size: 26px; line-height: 42px;
    color: var(--ink);
    -webkit-text-stroke: .4px var(--ink);
  }
  .extras {
    position: absolute;
    left: 88px; top: 562px;
    list-style: none;
    font-family: "Amaranth", sans-serif;
    font-style: italic; font-weight: 700;
    font-size: 20.5px; line-height: 30px;
    letter-spacing: .3px;
    color: var(--ink);
  }
  .extras li { padding-left: 14px; text-indent: -14px; }
  .extras li::before { content: "\2022\00a0"; }
  .extras .indent { display: block; text-indent: 0; padding-left: 4px; }
</style>
</head>
<body>
<main class="invitation">
  <section class="postcard-back" aria-label="Invitation back with party details">
    <svg class="sunburst" viewBox="0 0 1138 789" preserveAspectRatio="none" aria-hidden="true">
      <g fill="var(--teal-light)" opacity=".7">
        <polygon points="560,-150 0,120 0,330"/>
        <polygon points="560,-150 0,560 0,789 120,789"/>
        <polygon points="560,-150 420,789 640,789"/>
        <polygon points="560,-150 900,789 1138,789 1138,700"/>
        <polygon points="560,-150 1138,300 1138,480"/>
        <polygon points="560,-150 1138,0 1138,120"/>
      </g>
      <g fill="var(--teal-dark)" opacity=".35">
        <polygon points="560,-150 0,330 0,560"/>
        <polygon points="560,-150 640,789 900,789"/>
        <polygon points="560,-150 1138,120 1138,300"/>
      </g>
    </svg>

    <div class="illustration guitar-sketch" role="img" aria-label="Sketched acoustic guitar illustration"></div>
    <div class="illustration cactus-sketch" role="img" aria-label="Sketched saguaro cactus illustration"></div>
    <div class="illustration moustache-sketch" role="img" aria-label="Sketched handlebar moustache illustration"></div>

    <h1 class="title-name">DALE'S</h1>
    <p class="title-age">40th!</p>

    <div class="details">
      <div class="details-labels">
        <span>WHEN</span>
        <span>WHERE</span>
        <span>BRING</span>
        <span>RSVP</span>
      </div>
      <div class="details-divider"></div>
      <div class="details-values">
        <span>Saturday, July 27, 2013 at 7pm</span>
        <span>48 Marlow Crescent, Coromandel Valley, SA</span>
        <span>Yourself and Cowboy Drinkin’ Boots</span>
        <span>7.1.13, ilovetequila_and_nachos@fiestamail.com, 555.0148</span>
      </div>
    </div>

    <ul class="extras">
      <li>Preferred costumes are traditional Mexican or 70’s Cowboy/Girl, but tacky Sombreros<span class="indent">and Ponchos are OK too!</span></li>
      <li>There will be a prize for the best grown (real) Mexican moustache.</li>
      <li>Music by the Silver Cactus - Mexican Mariachi Band</li>
      <li>Food supplied by a delicious Mexican catering company</li>
      <li>Drinks by Bartender Trent. He’ll have the tequila shots and sangria ready to go!</li>
    </ul>
  </section>
</main>
</body>
</html>
```